Guaranteed Job - Sleek Sexy Business Card UV Spot

Im looking for a sleek and sexy business card, that resembles elite or VIP status status.
our business is corinvale.example
you can view our products on there, but our main audience for handing out our cards will be for people in the hospitality industry, so it will need to impress high management and CEO of hotels and restaurants, bars, clubs etc...
the card features will have UV spot on both sides, 400gsm stock. standard size.
Artwork should be 86 x 54mm + 2mm bleed = 90 x 58mm
it should have a nice "unique" uv spot pattern that highlights the card, not a repeated pattern, theres no originality there, and it will be disregarded.
The written material will be:
Corin Vale Hospitality College (logo)
Tobin Marsh
Director
Phone: 1300 615 737
Mobile: 0455 817 296
Email: info@corinvale.example
website: www.corinvale.example
I'm looking for originality here, i don't want just a simple stock card, want something that has a wow factor for people.
You will find the logo attached. you may invert the white to black words to suit the background as you please.
thank you and good luck
As a side note, ive received a lot of proposals, im too busy to give feedback to each and every one, so if i havent provided feedback for your design within 24 hours, then consider it not acceptable, and you could resubmit another design.
So far i have not seen any design that stood out for me, they all seem pretty generic. there nothing thats unique, i would figure for the amount that im offering, that people would put some more effort and creativity into the design.
so far over 200 designs submitted, and nothing i have seen looks very original, everything looks like a different variation of the same stuff, i said it very clearly i wanted something unique, the only thing that has come close to it so far is this one
Reason: Ive received alot of design concepts and i have reviewed everyone, but i havent had time to give feedback to every single one, only the ones that have interested me, if i havent responded, its because i havent found it good enough.
so far only a few design have been on par with what ive been looking for, an attractive eye popping design.
heres a few of them,
http://files.pixelbazaar.example/design_img/51736/62418/62418_2840915_51736_image.jpg
http://files.pixelbazaar.example/design_img/51736/68254/68254_2841377_51736_image.jpg
theyre, both unique and original, and eye catching, the only thing theyre missing is the sexyness.
if you still think you have some creativity left in your minds, then throw it on here.
Reason: Sorry guys for the delay, I was in a serious accident and out of commission for the past few months, I'm just slowly recovering now, please bare with me as i try to attend to this project, it may take me awhile as I have other projects that are on standby, I'm not 100% at the moment, so im extending the deadline for 2 weeks right now. Thanks for your patience.
Hospitality

```html
<!DOCTYPE html>
<html lang="en">
<head>
<meta charset="utf-8">
<title>Corin Vale Hospitality College – Business Card</title>
<link rel="stylesheet" href="https://fonts.googleapis.com/css2?family=Questrial&display=swap">
<style>
  :root {
    --backdrop: #7f918d;
    --card: #101112;
    --card-pattern: #18191b;
    --band: rgba(255, 255, 255, 0.12);
    --cyan: #4cb8e2;
    --ink: #ffffff;
    --muted: #9a9ea1;
    --font: "Questrial", "Century Gothic", sans-serif;
  }
  * { box-sizing: border-box; margin: 0; padding: 0; }
  html, body { width: 1200px; height: 600px; overflow: hidden; }
  body {
    background: var(--backdrop);
    font-family: var(--font);
    position: relative;
  }
  .card {
    position: absolute;
    top: 143px;
    width: 500px;
    height: 314px;
    background: var(--card);
    overflow: hidden;
    color: var(--ink);
  }
  .card--front { left: 60px;  border-radius: 157px 14px 14px 157px; }
  .card--back  { left: 640px; border-radius: 14px 157px 157px 14px; }

  .card__texture {
    position: absolute; inset: 0;
    background: radial-gradient(ellipse at 50% 50%, var(--card-pattern), var(--card) 75%);
  }

  /* Wordmark: invented name with one plain square */
  .wordmark { position: absolute; display: flex; align-items: center; gap: 14px; }
  .wordmark__square { width: 46px; height: 46px; background: var(--cyan); flex: none; }
  .wordmark__name {
    color: var(--ink);
    font-size: 19px;
    line-height: 1.15;
    letter-spacing: 0.5px;
    text-transform: uppercase;
  }

  /* Front */
  .front__band {
    position: absolute;
    left: 0; top: 100px;
    width: 330px; height: 86px;
    background: var(--band);
  }
  .card--front .wordmark { left: 120px; top: 112px; }
  .front__website {
    position: absolute;
    left: 130px; top: 210px;
    font-size: 21px;
    letter-spacing: 1.5px;
    color: var(--ink);
  }

  /* Back */
  .card--back .wordmark { left: 46px; top: 128px; }
  .card--back .wordmark__name { font-size: 17px; }
  .contact-person {
    position: absolute; left: 325px; top: 34px;
  }
  .contact-person__name { font-size: 17px; color: var(--cyan); letter-spacing: 0.4px; }
  .contact-person__role { font-size: 10px; color: var(--ink); margin-top: 2px; }
  .contact-list {
    position: absolute; left: 325px; top: 98px;
    list-style: none;
  }
  .contact-list__item {
    display: flex; align-items: center; gap: 10px;
    font-size: 10px; color: var(--ink);
    height: 17px;
  }
  .contact-list__icon {
    width: 11px; height: 11px; border-radius: 2px;
    background: var(--cyan); flex: none;
  }
  .contact-list__icon svg { display: block; width: 11px; height: 11px; }
</style>
</head>
<body>

  <section class="card card--front" aria-label="Card front">
    <div class="card__texture" role="img" aria-label="Faint tonal floral spot-UV pattern across the card"></div>
    <div class="front__band"></div>
    <div class="wordmark">
      <span class="wordmark__square"></span>
      <span class="wordmark__name">Corin Vale<br>Hospitality College</span>
    </div>
    <p class="front__website">www.corinvale.example</p>
  </section>

  <section class="card card--back" aria-label="Card back">
    <div class="card__texture" role="img" aria-label="Faint tonal floral spot-UV pattern across the card"></div>
    <div class="wordmark">
      <span class="wordmark__square"></span>
      <span class="wordmark__name">Corin Vale<br>Hospitality College</span>
    </div>
    <div class="contact-person">
      <p class="contact-person__name">Tobin Marsh</p>
      <p class="contact-person__role">Director</p>
    </div>
    <ul class="contact-list">
      <li class="contact-list__item">
        <span class="contact-list__icon"><svg viewBox="0 0 11 11"><rect x="3.5" y="2" width="4" height="7" rx="0.8" fill="none" stroke="#101112" stroke-width="1"/></svg></span>
        1300 615 737
      </li>
      <li class="contact-list__item">
        <span class="contact-list__icon"><svg viewBox="0 0 11 11"><path d="M3 2.5h2l.6 1.8-1 .8a5 5 0 0 0 1.8 1.8l.8-1 1.8.6v2a1 1 0 0 1-1 1A6 6 0 0 1 2 3.5a1 1 0 0 1 1-1z" fill="#101112"/></svg></span>
        0455 817 296
      </li>
      <li class="contact-list__item">
        <span class="contact-list__icon"><svg viewBox="0 0 11 11"><rect x="2" y="3" width="7" height="5" fill="none" stroke="#101112" stroke-width="1"/><path d="M2 3l3.5 3L9 3" fill="none" stroke="#101112" stroke-width="1"/></svg></span>
        info@corinvale.example
      </li>
      <li class="contact-list__item">
        <span class="contact-list__icon"><svg viewBox="0 0 11 11"><circle cx="5.5" cy="5.5" r="3.3" fill="none" stroke="#101112" stroke-width="1"/><path d="M2.2 5.5h6.6M5.5 2.2c-1.6 2-1.6 4.6 0 6.6M5.5 2.2c1.6 2 1.6 4.6 0 6.6" fill="none" stroke="#101112" stroke-width="0.8"/></svg></span>
        www.corinvale.example
      </li>
    </ul>
  </section>

</body>
</html>
```